Studying Effectively To Do List

I am looking to design a new "Study To Do List" for High School students (Ages 15 - 18) . This will be printed as an A4 notepad and so should only be a single A4 page.

The Design will need to be professional and look semi-serious but also be appealing to High school students (Ages 15 - 18) and should NOT be gender specific.

I have attached a word document outlining the structure of the page. The space provided should be large enough that people can write in it comfortably.

The notepad will most likely be printed in black and white but I'm also looking at coloured options - colours should be kept to a minimum.

This will be printed professionally and should also include a 3mm bleed.

The design should also include the business logo (included in the word document)

Target Market(s)

High School students (Ages 15 - 18). Both genders

Industry/Entity Type

Education

Font styles to use
Serif
Sans Serif

Requirements
Must have
• Please see the word document attached.
Should not have
• Too much colour

```html
<!DOCTYPE html>
<html lang="en">
<head>
<meta charset="utf-8">
<title>Study To Do List – Notepad Sheets</title>
<link href="https://fonts.googleapis.com/css2?family=Roboto:wght@400;700;900&display=swap" rel="stylesheet">
<style>
  :root{
    --backdrop:#c0c0c0;
    --paper:#ffffff;
    --rule:#555555;
    --row-tint:#ebebeb;
    --label-tint:#e2e2e2;
    --ink:#222222;
    --crop:#8a8a8a;
  }
  .theme-mono{ --accent:#a6a6a6; --dark:#333333; }
  .theme-colour{ --accent:#ff6a00; --dark:#1f3349; }

  *{box-sizing:border-box;margin:0;padding:0}
  html,body{width:1200px;height:850px;overflow:hidden}
  body{background:var(--backdrop);font-family:"Roboto",Arial,sans-serif;color:var(--ink);position:relative}

  .sheet{position:absolute;top:113px;width:445px;height:624px;transform:rotate(180deg);overflow:hidden}
  .sheet--mono{left:148px}
  .sheet--colour{left:667px}
  .page{position:absolute;left:0;top:0;width:519px;height:728px;background:var(--paper);transform:scale(.8574);transform-origin:0 0}

  /* crop marks */
  .crop{position:absolute;z-index:5;width:7px;height:7px;border-color:var(--crop);border-style:solid;border-width:0}
  .crop--tl{left:7px;top:7px;border-left-width:1px;border-top-width:1px}
  .crop--tr{right:7px;top:7px;border-right-width:1px;border-top-width:1px}
  .crop--bl{left:7px;bottom:7px;border-left-width:1px;border-bottom-width:1px}
  .crop--br{right:7px;bottom:7px;border-right-width:1px;border-bottom-width:1px}

  /* date band */
  .date-band{position:absolute;left:0;top:0}
  .date-label{position:absolute;left:20px;top:15px;font-weight:900;font-size:15px;letter-spacing:.5px;color:var(--ink)}
  .date-field{position:absolute;left:79px;top:16px;width:170px;height:24px;background:#fff;border:1px solid #999}

  /* brand mark */
  .brand{position:absolute;left:46px;top:100px;display:flex;align-items:center;gap:6px}
  .brand__dot{width:16px;height:16px;border-radius:50%;background:var(--accent)}
  .brand__name{font-weight:900;font-size:22px;color:var(--dark)}

  /* section tabs */
  .tab{position:absolute;height:10px;background:var(--dark);color:#fff;font-size:7px;font-weight:700;line-height:10px;text-align:center;letter-spacing:.3px}

  /* revision */
  .revision{position:absolute;left:198px;top:80px;width:283px;height:74px;border:1px solid var(--rule);display:grid;grid-template-columns:16px 122px 16px 1fr;grid-auto-rows:1fr}
  .revision span{font-size:7px;display:flex;align-items:center;justify-content:center}
  .revision .num{background:var(--dark);color:#fff}
  .revision .shade{background:var(--row-tint)}

  /* homework */
  .homework{position:absolute;left:39px;top:187px;width:442px;height:206px;border:1px solid var(--rule);display:grid;grid-auto-rows:1fr}
  .homework div{font-size:6px;padding:5px 0 0 3px}
  .homework div:nth-child(odd){background:var(--row-tint)}

  /* assessments */
  .assessments{position:absolute;left:39px;top:413px;width:442px;height:162px;border:1px solid var(--rule);display:grid;grid-auto-rows:1fr}
  .assessments .row{font-size:6px;padding-left:3px;display:flex;align-items:center;position:relative;border-bottom:1px solid #ccc}
  .assessments .row--assess{border-bottom:1px solid var(--rule)}
  .assessments .row:last-child{border-bottom:0}
  .assessments .lbl{background:var(--label-tint);padding:0 3px;line-height:9px}
  .assessments .due{position:absolute;left:270px;background:var(--label-tint);padding:0 4px;line-height:9px}

  /* notes / practice */
  .np-head{position:absolute;top:587px;height:20px;background:var(--dark);color:#fff;font-size:7px;font-weight:700;line-height:20px;text-align:center}
  .np-head--notes{left:39px;width:221px}
  .np-head--practice{left:261px;width:220px}
  .np-grid{position:absolute;top:607px;height:78px;border:1px solid var(--rule);border-top:0;display:grid;grid-auto-rows:1fr}
  .np-grid--notes{left:39px;width:222px;grid-template-columns:16px 92px 16px 1fr}
  .np-grid--practice{left:260px;width:221px;grid-template-columns:16px 1fr}
  .np-grid span{font-size:6px;border-bottom:1px solid #bbb;display:flex;align-items:center;justify-content:center}
  .np-grid .num{background:var(--label-tint)}
  .np-grid--notes span:nth-last-child(-n+4){border-bottom:0}
  .np-grid--practice span:nth-last-child(-n+2){border-bottom:0}

  /* footer web band */
  .web-band{position:absolute;left:0;top:700px}
  .web-text{position:absolute;left:280px;top:708px;width:208px;text-align:right;color:#fff;font-size:10px;font-weight:700;white-space:nowrap}
</style>
</head>
<body>

<section class="sheet sheet--mono theme-mono">
  <div class="page">
    <span class="crop crop--tl"></span><span class="crop crop--tr"></span><span class="crop crop--bl"></span><span class="crop crop--br"></span>

    <svg class="date-band" width="519" height="48" aria-hidden="true">
      <rect x="290" y="0" width="229" height="22" fill="var(--dark)"/>
      <polygon points="0,0 312,0 252,48 0,48" fill="var(--accent)"/>
    </svg>
    <span class="date-label">DATE:</span>
    <span class="date-field"></span>

    <div class="brand"><span class="brand__dot"></span><span class="brand__name">Tallowby</span></div>

    <div class="tab" style="left:198px;top:67px;width:56px">REVISION</div>
    <div class="revision">
      <span class="num">1</span><span></span><span class="num">5</span><span></span>
      <span class="num">2</span><span class="shade"></span><span class="num">6</span><span class="shade"></span>
      <span class="num">3</span><span></span><span class="num">7</span><span></span>
      <span class="num">4</span><span class="shade"></span><span class="num">8</span><span class="shade"></span>
    </div>

    <div class="tab" style="left:39px;top:177px;width:56px">HOMEWORK</div>
    <div class="homework">
      <div>Subject:</div><div>Task:</div><div>Subject:</div><div>Task:</div>
      <div>Subject:</div><div>Task:</div><div>Subject:</div><div>Subject:</div>
      <div>Task:</div><div>Subject:</div><div>Task:</div>
    </div>

    <div class="tab" style="left:39px;top:403px;width:60px">ASSESSMENTS</div>
    <div class="assessments">
      <div class="row row--assess"><span class="lbl">Assessment:</span><span class="due">Due</span></div><div class="row"><span>Element:</span></div>
      <div class="row row--assess"><span class="lbl">Assessment:</span><span class="due">Due</span></div><div class="row"><span>Element:</span></div>
      <div class="row row--assess"><span class="lbl">Assessment:</span><span class="due">Due</span></div><div class="row"><span>Element:</span></div>
      <div class="row row--assess"><span class="lbl">Assessment:</span><span class="due">Due</span></div><div class="row"><span>Element:</span></div>
      <div class="row row--assess"><span class="lbl">Assessment:</span><span class="due">Due</span></div><div class="row"><span>Element:</span></div>
      <div class="row row--assess"><span class="lbl">Assessment:</span><span class="due">Due</span></div><div class="row"><span>Element:</span></div>
    </div>

    <div class="np-head np-head--notes">NOTES</div>
    <div class="np-head np-head--practice">PRACTICE</div>
    <div class="np-grid np-grid--notes">
      <span class="num">1</span><span></span><span class="num">5</span><span></span>
      <span class="num">2</span><span></span><span class="num">6</span><span></span>
      <span class="num">3</span><span></span><span class="num">7</span><span></span>
      <span class="num">4</span><span></span><span class="num">8</span><span></span>
    </div>
    <div class="np-grid np-grid--practice">
      <span class="num">1</span><span></span>
      <span class="num">2</span><span></span>
      <span class="num">3</span><span></span>
      <span class="num">4</span><span></span>
    </div>

    <svg class="web-band" width="519" height="28" aria-hidden="true">
      <polygon points="262,0 519,0 519,28 302,28" fill="var(--accent)"/>
      <polygon points="246,0 262,0 302,28 286,28" fill="var(--dark)"/>
    </svg>
    <span class="web-text">www.tallowbystudy.example</span>
  </div>
</section>

<section class="sheet sheet--colour theme-colour">
  <div class="page">
    <span class="crop crop--tl"></span><span class="crop crop--tr"></span><span class="crop crop--bl"></span><span class="crop crop--br"></span>

    <svg class="date-band" width="519" height="48" aria-hidden="true">
      <rect x="290" y="0" width="229" height="22" fill="var(--dark)"/>
      <polygon points="0,0 312,0 252,48 0,48" fill="var(--accent)"/>
    </svg>
    <span class="date-label">DATE:</span>
    <span class="date-field"></span>

    <div class="brand"><span class="brand__dot"></span><span class="brand__name">Tallowby</span></div>

    <div class="tab" style="left:198px;top:67px;width:56px">REVISION</div>
    <div class="revision">
      <span class="num">1</span><span></span><span class="num">5</span><span></span>
      <span class="num">2</span><span class="shade"></span><span class="num">6</span><span class="shade"></span>
      <span class="num">3</span><span></span><span class="num">7</span><span></span>
      <span class="num">4</span><span class="shade"></span><span class="num">8</span><span class="shade"></span>
    </div>

    <div class="tab" style="left:39px;top:177px;width:56px">HOMEWORK</div>
    <div class="homework">
      <div>Subject:</div><div>Task:</div><div>Subject:</div><div>Task:</div>
      <div>Subject:</div><div>Task:</div><div>Subject:</div><div>Subject:</div>
      <div>Task:</div><div>Subject:</div><div>Task:</div>
    </div>

    <div class="tab" style="left:39px;top:403px;width:60px">ASSESSMENTS</div>
    <div class="assessments">
      <div class="row row--assess"><span class="lbl">Assessment:</span><span class="due">Due</span></div><div class="row"><span>Element:</span></div>
      <div class="row row--assess"><span class="lbl">Assessment:</span><span class="due">Due</span></div><div class="row"><span>Element:</span></div>
      <div class="row row--assess"><span class="lbl">Assessment:</span><span class="due">Due</span></div><div class="row"><span>Element:</span></div>
      <div class="row row--assess"><span class="lbl">Assessment:</span><span class="due">Due</span></div><div class="row"><span>Element:</span></div>
      <div class="row row--assess"><span class="lbl">Assessment:</span><span class="due">Due</span></div><div class="row"><span>Element:</span></div>
      <div class="row row--assess"><span class="lbl">Assessment:</span><span class="due">Due</span></div><div class="row"><span>Element:</span></div>
    </div>

    <div class="np-head np-head--notes">NOTES</div>
    <div class="np-head np-head--practice">PRACTICE</div>
    <div class="np-grid np-grid--notes">
      <span class="num">1</span><span></span><span class="num">5</span><span></span>
      <span class="num">2</span><span></span><span class="num">6</span><span></span>
      <span class="num">3</span><span></span><span class="num">7</span><span></span>
      <span class="num">4</span><span></span><span class="num">8</span><span></span>
    </div>
    <div class="np-grid np-grid--practice">
      <span class="num">1</span><span></span>
      <span class="num">2</span><span></span>
      <span class="num">3</span><span></span>
      <span class="num">4</span><span></span>
    </div>

    <svg class="web-band" width="519" height="28" aria-hidden="true">
      <polygon points="262,0 519,0 519,28 302,28" fill="var(--accent)"/>
      <polygon points="246,0 262,0 302,28 286,28" fill="var(--dark)"/>
    </svg>
    <span class="web-text">www.tallowbystudy.example</span>
  </div>
</section>

</body>
</html>
```